Website design for Cloud Scheduling Company

We have a design build that is based on a corporate template. the structure and content is there but the design does not match the 'feel' of what we are going for from a design perspective.
http://plumvexo.com/demo/fen/

please follow this structure for the site layout but add new ideas also.

Scheduling is boring and typically a serious topic, with our new logo we are looking to bring a quirky, fun feeling to what our site does.

It is a powerful scheduling platform that is used mainly in Volunteer environments and we want our brand to reflect this.

A lot of sites use images of real people in photographs but i would like to see us use more vector graphics and illustrations in the design so it is a bit more exciting.

The homepage should have a large screen capture of the app on different devices (large monitor, tablet, and smartphone) which is pretty standard for this type of website.i have attached a jpeg where you can get images from as well as the logo so you can get a sense of the look and feel.

this is what I envision being the image in the main banner as it showcases the application https://www.trindlesk.ca/search?q=responsive&biw=1920&bih=920&source=lnms&tbm=isch&sa=X&ved=0ahUKEwiAlqahjv_KAhXrlIMKHToqB5oQ_AUIBigB#imgrc=a75LOlLuwcKyqM%3A

Again, what I need for this project is a design for the site at http://plumvexo.com/demo/fen/. it is already coded but i need a netter design. focus on homepage, pricing page and a general subpage please.

Target Market(s)

Volunteer organization Administrators

Industry/Entity Type

It Company

Number of Pages Required

3 page

Font styles to use
Sans Serif

Colors
0355a3
f37122

Requirements
Nice to have
• use graphics instead of photographs. you can include some photos but i want the look and feel to be consistent with the playfulness of the logo so the site isnt too serious. The site still has to be professional.

```html
<!DOCTYPE html>
<html lang="en">
<head>
<meta charset="utf-8">
<title>Fen Roster — Cloud Scheduling</title>
<link rel="stylesheet" href="https://fonts.googleapis.com/css2?family=Open+Sans:wght@400;600;700&family=Raleway:wght@300;400;600&display=swap">
<style>
:root{
  --blue:#0355a3;
  --orange:#f37122;
  --ink:#333;
  --muted:#777;
  --line:#e4e4e4;
  --soft:#f4f4f4;
  --dark:#2b2b2b;
  --darker:#1f1f1f;
  --footer:#3a3a3a;
}
*{box-sizing:border-box;margin:0;padding:0}
html,body{width:1200px;height:3087px;overflow:hidden}
body{font-family:"Open Sans",Arial,sans-serif;color:var(--ink);background:#fff;font-size:11px;line-height:1.6;position:relative}
.head-font{font-family:"Raleway","Helvetica Neue",sans-serif}
.wrap{width:660px;margin:0 auto;position:relative}
section,header,footer{position:absolute;left:0;width:1200px}

/* top bar + header */
.topbar{top:0;height:25px;border-bottom:1px solid var(--line);font-size:8px;color:var(--muted);line-height:25px}
.site-header{top:25px;height:53px;border-bottom:1px solid var(--line)}
.brand{position:absolute;left:0;top:12px;display:flex;align-items:center;gap:8px}
.brand-mark{width:26px;height:26px;background:var(--blue);border-radius:50%}
.brand-name{font-family:"Open Sans",sans-serif;font-weight:700;font-size:21px;color:var(--blue)}
.nav{position:absolute;right:0;top:18px;display:flex;gap:28px;font-size:10px;color:#555}

/* hero */
.hero{top:78px;height:385px;background:var(--soft);text-align:center}
.hero-kicker{padding-top:44px;color:var(--orange);font-size:15px}
.hero-title{color:var(--blue);font-size:21px;letter-spacing:1px;margin-top:6px}
.hero-sub{font-size:10px;color:#666;margin-top:4px}
.hero-shot{position:absolute;left:330px;top:128px;width:535px;height:257px;border-radius:12px 12px 0 0;background:linear-gradient(180deg,#e9e9ea,#d4d6da)}

/* features */
.features{top:463px;height:300px}
.feature{position:absolute;top:52px;width:210px;height:195px;padding:30px 24px 0}
.feature h3{font-size:11px;font-weight:600;letter-spacing:.3px;margin-top:10px}
.feature p{font-size:9px;color:#666;margin-top:4px}
.feature .more{font-size:7px;color:#888;margin-top:14px;display:inline-block}
.feature.is-active{background:var(--orange);color:#fff}
.feature.is-active p,.feature.is-active .more{color:#fff}
.feature.is-active .more{border-bottom:1px solid #fff;padding-bottom:2px}
.rule{position:absolute;left:270px;width:660px;height:1px;background:var(--line)}

/* about */
.about{top:792px;height:300px}
.section-title{font-family:"Raleway",sans-serif;font-weight:400;font-size:17px;color:#444}
.lead{color:var(--blue);font-weight:600;font-size:10px;margin-top:12px;line-height:1.55}
.body-copy{font-size:9px;color:#777;margin-top:12px;line-height:1.65}
.btn{display:inline-flex;height:27px;font-size:9px;font-weight:600;color:#fff;margin-top:28px}
.btn span{background:var(--orange);padding:0 16px;line-height:27px}
.btn i{background:#333;width:27px;display:flex;align-items:center;justify-content:center}
.about-col{position:absolute;left:0;top:0;width:260px}
.mini{position:absolute;width:140px}
.mini h4{font-size:10px;font-weight:400;margin-top:6px;color:#444}
.mini hr{border:0;border-top:1px solid var(--orange);width:80px;margin:7px 0}
.mini p{font-size:8px;color:#888;line-height:1.6}

/* benefits */
.benefits{top:1122px;height:453px;background:var(--soft)}
.benefits .section-title{text-align:center;padding-top:54px}
.laptop{position:absolute;left:270px;top:116px;width:314px;height:180px;border-radius:6px;background:linear-gradient(180deg,#2c2c2c,#4a4a4a)}
.benefit-col{position:absolute;left:620px;top:110px;width:310px}
.benefit-col .intro{font-size:9px;color:#444;line-height:1.55}
.benefit{display:flex;gap:8px;margin-top:11px;font-size:8px;color:#666;line-height:1.5}
.benefit b{color:var(--blue)}
.tick{flex:0 0 10px;margin-top:2px}

/* clients */
.clients{top:1616px;height:190px;text-align:center}
.clients .sub{font-size:9px;color:#999;width:420px;margin:8px auto 0;line-height:1.55}
.client-row{display:flex;justify-content:space-between;width:560px;margin:26px auto 0;font-weight:600;font-size:15px;color:#555}

/* responsive */
.responsive{top:1842px;height:240px}
.responsive-copy{position:absolute;left:0;top:0;width:360px}
.devices{position:absolute;left:390px;top:10px;width:270px;height:205px;background:linear-gradient(180deg,#ededef,#d8dade);border-radius:8px}

/* work hard */
.workhard{top:2124px;height:381px;background:linear-gradient(135deg,#3a3a3a,#1e1e1e);color:#fff;text-align:center}
.workhard h2{font-family:"Raleway",sans-serif;font-weight:400;font-size:17px;padding-top:52px}
.workhard .sub{font-size:9px;color:#ccc}
.work-card{position:absolute;top:123px;width:208px;height:204px;background:rgba(20,20,20,.82);text-align:left;padding:40px 28px 0}
.work-card h3{font-size:11px;font-weight:600;margin-top:12px}
.work-card p{font-size:8px;color:#ccc;margin-top:6px;line-height:1.6}
.work-card .more{font-size:7px;color:#aaa;margin-top:14px;display:block}

/* blog + testimonial */
.lower{top:2542px;height:308px}
.post-date{font-size:8px;color:#888;margin-top:28px}
.post-title{color:var(--blue);font-weight:600;font-size:10px;margin-top:10px;line-height:1.45}
.post-meta{display:flex;gap:20px;font-size:7px;color:var(--blue);border-top:1px solid var(--line);border-bottom:1px solid var(--line);padding:7px 0;margin-top:16px;width:250px}
.quote{background:var(--soft);padding:18px 16px;font-size:8.5px;color:#555;margin-top:24px;line-height:1.6}
.person{display:flex;gap:12px;margin-top:14px}
.avatar{width:46px;height:46px;border-radius:50%;background:#bcbcbc}
.person b{font-size:9px}
.person small{display:block;font-size:7px;color:#888;line-height:1.5}

/* footer */
.site-footer{top:2850px;height:216px;background:var(--footer);color:#ddd}
.fcol{position:absolute;top:50px}
.fcol h5{font-size:10px;font-weight:600;color:#fff;margin-bottom:14px}
.fitem{display:flex;gap:8px;font-size:7.5px;color:#bbb;margin-bottom:10px;line-height:1.45}
.fitem svg{flex:0 0 auto;margin-top:1px}
.email-box{display:flex;width:166px;height:26px;border:1px solid #666;margin-top:12px;font-size:7.5px;color:#aaa;align-items:center;justify-content:space-between;padding:0 8px}
.email-box i{width:18px;height:10px;background:var(--orange)}
.socials{display:flex;gap:10px}
.socials i{width:11px;height:11px;background:#aaa;border-radius:50%}
.bottombar{top:3066px;height:21px;background:var(--darker);font-size:7px;color:#888;line-height:21px}
</style>
</head>
<body>

<header class="topbar"><div class="wrap">Call Us: (555) 010-4420 · Mail: info@example.com</div></header>

<header class="site-header">
  <div class="wrap">
    <div class="brand"><span class="brand-mark"></span><span class="brand-name">fenroster</span></div>
    <nav class="nav"><span>Home</span><span>About Us</span><span>Services</span><span>Pricing</span><span>Blog</span><span>Contact Us</span>
      <svg width="10" height="10" viewBox="0 0 10 10"><circle cx="4" cy="4" r="3" fill="none" stroke="#777" stroke-width="1.2"/><path d="M6.3 6.3 9 9" stroke="#777" stroke-width="1.2"/></svg>
    </nav>
  </div>
</header>

<section class="hero">
  <p class="hero-kicker head-font">Free YourSelf From</p>
  <h1 class="hero-title head-font" style="font-weight:400">MUNDANE REPETITIVE SCHEDULING</h1>
  <p class="hero-sub">Fen Roster makes the Scheduling process simple for you and ever simple for your Volunteers</p>
  <div class="hero-shot" role="img" aria-label="Screenshots of the scheduling app on a desktop monitor, a tablet and a smartphone"></div>
</section>

<section class="features">
  <div class="feature" style="left:290px">
    <svg width="22" height="30" viewBox="0 0 22 30"><rect x="3" y="1" width="16" height="28" rx="2" fill="none" stroke="#666" stroke-width="1.4"/><line x1="9" y1="25" x2="13" y2="25" stroke="#666" stroke-width="1.4"/></svg>
    <h3>WEB AND MOBILE READY</h3>
    <p>Schedule at your desk or on the go.</p>
    <span class="more">READ MORE</span>
  </div>
  <div class="feature is-active" style="left:495px">
    <svg width="30" height="30" viewBox="0 0 30 30"><path d="M20 8 10 18a3 3 0 0 0 4 4l11-11a5 5 0 0 0-7-7L7 15a7 7 0 0 0 10 10l8-8" fill="none" stroke="#fff" stroke-width="1.8" stroke-linecap="round"/></svg>
    <h3>INCEREBLY FLEXIBLE</h3>
    <p>Manage 10 Volunteers or 1000.</p>
    <span class="more">READ MORE</span>
  </div>
  <div class="feature" style="left:725px">
    <svg width="30" height="30" viewBox="0 0 30 30"><circle cx="15" cy="15" r="5" fill="none" stroke="#666" stroke-width="1.4"/><circle cx="15" cy="15" r="10" fill="none" stroke="#666" stroke-width="1.4" stroke-dasharray="4 3"/></svg>
    <h3>FREE UPGRADES &amp; SUPPORT</h3>
    <p>Maintenance fees are a thing of the past.</p>
    <span class="more">READ MORE</span>
  </div>
  <div class="rule" style="top:300px"></div>
</section>

<section class="about">
  <div class="wrap">
    <div class="about-col">
      <h2 class="section-title">About Us</h2>
      <p class="lead">Lorem ipsum dolor sit amet, consectetuer adipiscing elit. Aenean commodo ligula eget dolor. Aenean massa.</p>
      <p class="body-copy">Nulla consequat massa quis enim. Donec pede justo, fringilla vel, aliquet nec, vulputate eget, arcu. In enim justo, rhoncus ut, imperdiet a, venenatis vitae, justo. Nullam dictum felis eu pede mollis pretium. Integer tincidunt. Cras dapibus. Vivamus elementum semper nisi. Aenean vulputate eleifend tellus.</p>
      <a class="btn"><span>LEARN MORE</span><i><svg width="6" height="9" viewBox="0 0 6 9"><path d="M1 1l3.5 3.5L1 8" fill="none" stroke="#fff" stroke-width="1.4"/></svg></i></a>
    </div>
    <div class="mini" style="left:330px;top:0">
      <svg width="22" height="22" viewBox="0 0 22 22"><circle cx="11" cy="11" r="3" fill="#555"/><circle cx="3" cy="4" r="2" fill="#555"/><circle cx="19" cy="5" r="2" fill="#555"/><circle cx="6" cy="19" r="2" fill="#555"/><path d="M3 4l8 7 8-6M11 11l-5 8" stroke="#555"/></svg>
      <h4>HTML5 / CSS3 / JS</h4><hr><p>Aenean vulputate eleifend tellus. Aenean leo ligula, porttitor eu, consequat vitae, eleifend ac, enim.</p>
    </div>
    <div class="mini" style="left:520px;top:0">
      <svg width="24" height="22" viewBox="0 0 24 22"><rect x="2" y="2" width="20" height="14" rx="1" fill="none" stroke="#555" stroke-width="1.4"/><path d="M12 16v4M7 20h10" stroke="#555" stroke-width="1.4"/></svg>
      <h4>Awesome Sliders</h4><hr><p>Aenean vulputate eleifend tellus. Aenean leo ligula, porttitor eu, consequat vitae, eleifend ac, enim.</p>
    </div>
    <div class="mini" style="left:330px;top:148px">
      <svg width="22" height="22" viewBox="0 0 22 22"><path d="M3 19l7-7M12 4l6 6-6 4-4-4z" fill="none" stroke="#555" stroke-width="1.4"/></svg>
      <h4>Clean Design</h4><hr><p>Aenean vulputate eleifend tellus. Aenean leo ligula, porttitor eu, consequat vitae, eleifend ac, enim.</p>
    </div>
    <div class="mini" style="left:520px;top:148px">
      <svg width="22" height="22" viewBox="0 0 22 22"><circle cx="9" cy="9" r="6" fill="none" stroke="#555" stroke-width="1.4"/><path d="M13.5 13.5 20 20M9 6v6M6 9h6" stroke="#555" stroke-width="1.4"/></svg>
      <h4>Other Features</h4><hr><p>Aenean vulputate eleifend tellus. Aenean leo ligula, porttitor eu, consequat vitae, eleifend ac, enim.</p>
    </div>
  </div>
</section>

<section class="benefits">
  <h2 class="section-title">Your Benifits Include</h2>
  <div class="laptop" role="img" aria-label="Laptop showing the Fen Roster homepage"></div>
  <div class="benefit-col">
    <p class="intro">Our core speciality is solving business problems that require complex data analysis, cleansing, mining or modelling techniques. Your benefits include:</p>
    <div class="benefit"><svg class="tick" width="10" height="9" viewBox="0 0 10 9"><path d="M1 4.5 4 7.5 9 1" fill="none" stroke="#333" stroke-width="1.6"/></svg><span><b>Fast ROI</b>: Quick access to skilled data professionals, without the overhead of building and maintaining your own infrastructure and team.</span></div>
    <div class="benefit"><svg class="tick" width="10" height="9" viewBox="0 0 10 9"><path d="M1 4.5 4 7.5 9 1" fill="none" stroke="#333" stroke-width="1.6"/></svg><span><b>Innovative practical solutions</b>: We find smart ways to extract useful information from incomplete and disorganised data.</span></div>
    <div class="benefit"><svg class="tick" width="10" height="9" viewBox="0 0 10 9"><path d="M1 4.5 4 7.5 9 1" fill="none" stroke="#333" stroke-width="1.6"/></svg><span><b>Connected to major universities</b>: We have relationships with leading practitioners at major universities and business schools within Australia.</span></div>
    <div class="benefit"><svg class="tick" width="10" height="9" viewBox="0 0 10 9"><path d="M1 4.5 4 7.5 9 1" fill="none" stroke="#333" stroke-width="1.6"/></svg><span><b>Always confidential and discreet.</b></span></div>
    <div class="benefit"><svg class="tick" width="10" height="9" viewBox="0 0 10 9"><path d="M1 4.5 4 7.5 9 1" fill="none" stroke="#333" stroke-width="1.6"/></svg><span><b>Connected to major universities</b>: We have relationships with leading practitioners at major universities and business schools within Australia.</span></div>
    <a class="btn" style="margin-top:22px"><span>LEARN MORE</span><i><svg width="6" height="9" viewBox="0 0 6 9"><path d="M1 1l3.5 3.5L1 8" fill="none" stroke="#fff" stroke-width="1.4"/></svg></i></a>
  </div>
</section>

<section class="clients">
  <h2 class="section-title">Our Happy Clients</h2>
  <p class="sub">Lorem ipsum dolor sit amet, consectetuer adipiscing elit, sed diam nonummy nibh euismod tincidunt ut laoreet dolore magna aliquam erat volutpat.</p>
  <div class="client-row"><span>Norvel</span><span>Brisk</span><span>Kelto</span><span>Mavra</span><span>Ostlund</span></div>
  <div class="rule" style="top:189px"></div>
</section>

<section class="responsive">
  <div class="wrap">
    <div class="responsive-copy">
      <h2 class="section-title">Ultra-Responsive Design</h2>
      <p class="lead">Lorem ipsum dolor sit amet, consectetuer adipiscing elit, sed diam nonummy nibh euismod tincidunt ut laoreet dolore magna aliquam erat volutpat.</p>
      <p class="body-copy">Lui vel laborum dolo numes fugats untras. Etha rums ser quidem rerum facilis dolores nemis omis fugats vitaes nemo minima rerums unsers sadips amets. Ut enim ad minim veniam, quis nostrud Neque porro quisquam est, qui dolorem ipsum quia dolor sit amet, consectetur, adipisci velit.</p>
      <p class="body-copy">Etharums ser quidem rerum facilis dolores nemis omnis fugats vitaes nemo minima rerums unsers sadips ameet quasi architecto beatae vitae dicta sunt explicabo.</p>
      <a class="btn" style="margin-top:18px"><span>LEARN MORE</span><i><svg width="6" height="9" viewBox="0 0 6 9"><path d="M1 1l3.5 3.5L1 8" fill="none" stroke="#fff" stroke-width="1.4"/></svg></i></a>
    </div>
    <div class="devices" role="img" aria-label="Dashboard shown on a desktop monitor, a tablet and a phone"></div>
  </div>
</section>

<section class="workhard" role="img" aria-label="Dark desk scene with glasses, a coffee cup and hand-drawn sketches">
  <h2>We Work Hard For You</h2>
  <p class="sub">Try new experience with Fen Roster</p>
  <div class="work-card" style="left:270px">
    <svg width="28" height="26" viewBox="0 0 28 26"><rect x="2" y="2" width="24" height="16" fill="none" stroke="#fff" stroke-width="1.6"/><path d="M14 18v5M8 23h12M8 13l5-5 3 3 5-5" fill="none" stroke="#fff" stroke-width="1.6"/></svg>
    <h3>DESIGN</h3><p>Import your Volunteer list and Build Your Schedule</p><span class="more">READ MORE</span>
  </div>
  <div class="work-card" style="left:496px">
    <svg width="28" height="26" viewBox="0 0 28 26"><rect x="2" y="2" width="24" height="20" fill="none" stroke="#fff" stroke-width="1.6"/><path d="M2 7h24M10 12l-3 3 3 3M18 12l3 3-3 3" fill="none" stroke="#fff" stroke-width="1.6"/></svg>
    <h3>DEVELOP</h3><p>Our team can assist in importing your volunteer list if its too large</p><span class="more">READ MORE</span>
  </div>
  <div class="work-card" style="left:722px">
    <svg width="30" height="26" viewBox="0 0 30 26"><path d="M2 10l7-6 6 4 6-4 7 6-8 9-5-4-5 4z" fill="none" stroke="#fff" stroke-width="1.6" stroke-linejoin="round"/></svg>
    <h3>SUPPORT</h3><p>A simple email out to volunteers will let them know that the schedule</p><span class="more">READ MORE</span>
  </div>
</section>

<section class="lower">
  <div class="wrap">
    <div style="position:absolute;left:0;width:260px">
      <h2 class="section-title">Latest Blog Posts</h2>
      <p class="post-date">▦ &nbsp;January 11, 2016</p>
      <p class="post-title">Lorem ipsum dolor sit amet, consectetur adipiscing elit.</p>
      <p class="body-copy" style="margin-top:8px">Lorem ipsum dolor sit amet, consectetur adipiscing elit. Donec hendrerit vehicula est, in consequat libero.</p>
      <div class="post-meta"><span>By Dan Morrow</span><span>Design , Lifestyle</span><span>26 Comments</span></div>
      <a class="btn" style="margin-top:16px"><span>READ MORE</span><i><svg width="6" height="9" viewBox="0 0 6 9"><path d="M1 1l3.5 3.5L1 8" fill="none" stroke="#fff" stroke-width="1.4"/></svg></i></a>
    </div>
    <div style="position:absolute;left:330px;width:330px">
      <h2 class="section-title">What Client's Say</h2>
      <p class="quote">"I have continue to work with them in my new Administrator role with Ridgeway Civic Services. Their attention to detail and ability to understand complex operational items really helps them in to produce great work."</p>
      <div class="person"><div class="avatar" role="img" aria-label="Client portrait"></div><div><b>Marla J. Hewitt</b><small>Visitor Services Administrator</small><small>Ridgeway Civic Services</small></div></div>
      <a class="btn" style="margin-top:14px"><span>READ MORE</span><i><svg width="6" height="9" viewBox="0 0 6 9"><path d="M1 1l3.5 3.5L1 8" fill="none" stroke="#fff" stroke-width="1.4"/></svg></i></a>
    </div>
  </div>
</section>

<footer class="site-footer">
  <div class="wrap">
    <div class="fcol" style="left:0;width:150px">
      <h5>Newsletter</h5>
      <div class="fitem"><svg width="8" height="10" viewBox="0 0 8 10"><path d="M4 10S1 6 1 4a3 3 0 0 1 6 0c0 2-3 6-3 6z" fill="#bbb"/></svg><span>CCM Street Name, City Name<br>United States</span></div>
      <div class="fitem"><svg width="9" height="9" viewBox="0 0 9 9"><path d="M2 1l2 2-1 1.5a5 5 0 0 0 1.5 1.5L6 5l2 2-1.5 1.5C4 8 1 5 .5 2z" fill="#bbb"/></svg><span>(555) 010-4420</span></div>
      <div class="fitem"><svg width="9" height="8" viewBox="0 0 9 8"><rect x=".5" y=".5" width="8" height="7" fill="none" stroke="#bbb"/><path d="M.5 .5l4 4 4-4" fill="none" stroke="#bbb"/></svg><span>mail@example.com</span></div>
    </div>
    <div class="fcol" style="left:170px;width:170px">
      <h5>Newsletter</h5>
      <p class="fitem">Lorem ipsum dolor sit amet, consectetur adipiscing elit. Donec hendrerit vehicula est, in consequat.</p>
      <div class="email-box">Email Address<i></i></div>
    </div>
    <div class="fcol" style="left:370px;width:140px">
      <h5>Latest Tweet</h5>
      <div class="fitem"><svg width="9" height="8" viewBox="0 0 9 8"><rect width="9" height="8" rx="2" fill="#bbb"/></svg><span>Lorem ipsum dolor sit amet, consectetur adipiscing elit. Donec.<br>2 min ago</span></div>
      <div class="fitem"><svg width="9" height="8" viewBox="0 0 9 8"><rect width="9" height="8" rx="2" fill="#bbb"/></svg><span>Lorem ipsum dolor sit amet, consectetur adipiscing elit. Donec.<br>2 min ago</span></div>
    </div>
    <div class="fcol" style="left:550px;width:110px">
      <h5>Social Links</h5>
      <div class="socials"><i></i><i></i><i></i></div>
    </div>
  </div>
</footer>
<footer class="bottombar"><div class="wrap">Copyright © 2016 Fen Roster. All Rights Reserved.<span style="position:absolute;right:0">FAQ's &nbsp;|&nbsp; Sitemap &nbsp;|&nbsp; Contact</span></div></footer>

</body>
</html>
```